Business car for dental practice

I have a new logo. Want it use for a new business card design. Hi end dental practice Would like a scan code on it for quick access to my web site and mobile site too. Green and purple are in logo design. Maybe have scan code on back? My website is peterhalvorsenDDS.example
Updates

Lakemont Crest Dental Associates

248 N Fairlawn Ave
Harlow Glen, ST 00412
555-318-4072

317 N Wexford Rd. 
Suite 406
Mt. Verity, ST 00587
555-762-1938

would like to incorporate logo, and addresses of both offices, and I recently saw a business card with a scan box on it which would bring people directly to the web site. if anyone knows how to do that, that could possibly go on the back of the card. (May be something I have to add at printing process) card can be one sided, or two sided.  

Reason: designer is revising for me. has not posted changes yet. hope he does soon!!

Industry/Entity Type

Business

```html
<!DOCTYPE html>
<html lang="en">
<head>
<meta charset="utf-8">
<title>Lakemont Crest Dental Associates – Business Card</title>
<link rel="stylesheet" href="https://fonts.googleapis.com/css2?family=EB+Garamond:wght@400&family=Roboto+Condensed:wght@300;400&display=swap">
<style>
  :root {
    --card-white: #ffffff;
    --gutter-black: #000000;
    --plum: #5a2a56;
    --plum-mark: #7b2a6f;
    --leaf-green: #4b8c3f;
    --ink-light: #ffffff;
    --name-ink: #4a2347;
  }
  * { margin: 0; padding: 0; box-sizing: border-box; }
  html, body {
    width: 1200px;
    height: 345px;
    overflow: hidden;
    background: var(--gutter-black);
  }
  .sheet {
    position: relative;
    width: 1200px;
    height: 345px;
  }
  .card-front {
    position: absolute;
    left: 0; top: 0;
    width: 588px; height: 345px;
    background: var(--card-white);
  }
  .card-back {
    position: absolute;
    left: 618px; top: 0;
    width: 582px; height: 345px;
    background: var(--plum);
    color: var(--ink-light);
  }

  /* Front: practice name */
  .front-brand {
    position: absolute;
    left: 130px; top: 140px;
    display: flex;
    align-items: center;
    gap: 8px;
    color: var(--plum-mark);
    font-family: "EB Garamond", serif;
    font-weight: 400;
  }
  .front-brand__square {
    width: 58px; height: 58px;
    background: var(--plum-mark);
    flex: none;
  }
  .front-brand__name {
    display: block;
    font-size: 42px;
    line-height: 1;
  }
  .front-brand__sub {
    display: block;
    font-size: 16px;
    letter-spacing: 3.4px;
    line-height: 1;
    margin-top: 2px;
    padding-left: 24px;
  }

  /* Back */
  .back-brand {
    position: absolute;
    left: 42px; top: 40px;
    font-family: "EB Garamond", serif;
    font-weight: 400;
  }
  .back-brand__name {
    display: block;
    font-size: 31px;
    line-height: 1;
  }
  .back-brand__sub {
    display: block;
    font-size: 15px;
    letter-spacing: 3px;
    margin-top: 8px;
  }
  .doctor-band {
    position: absolute;
    left: 0; top: 128px;
    width: 297px; height: 45px;
    background: var(--leaf-green);
    color: var(--name-ink);
    font-family: "Roboto Condensed", sans-serif;
    font-weight: 400;
    font-size: 21px;
    line-height: 45px;
    padding-left: 40px;
    white-space: nowrap;
  }
  .website {
    position: absolute;
    left: 0; top: 196px;
    width: 297px;
    text-align: center;
    font-family: "Roboto Condensed", sans-serif;
    font-weight: 300;
    font-size: 22px;
    white-space: nowrap;
  }
  .scan-box {
    position: absolute;
    left: 122px; top: 248px;
    width: 58px; height: 57px;
    background: var(--card-white);
  }
  .offices {
    position: absolute;
    left: 354px; top: 44px;
    font-family: "Roboto Condensed", sans-serif;
    font-weight: 300;
    font-size: 23px;
    line-height: 32.5px;
    white-space: nowrap;
  }
  .office { font-style: normal; }
  .office + .office { margin-top: 28px; }
</style>
</head>
<body>
<main class="sheet">
  <section class="card-front" aria-label="Card front">
    <div class="front-brand">
      <span class="front-brand__square" aria-hidden="true"></span>
      <div>
        <span class="front-brand__name">Lakemont Crest</span>
        <span class="front-brand__sub">Dental Associates</span>
      </div>
    </div>
  </section>

  <section class="card-back" aria-label="Card back">
    <div class="back-brand">
      <span class="back-brand__name">Lakemont Crest</span>
      <span class="back-brand__sub">Dental Associates</span>
    </div>
    <div class="doctor-band">Dr. Peter Halvorsen, DDS</div>
    <div class="website">peterhalvorsenDDS.example</div>
    <div class="scan-box" role="img" aria-label="Scan code area for the practice website"></div>
    <div class="offices">
      <address class="office">
        248 N Fairlawn Ave<br>
        Harlow Glen, ST 00412<br>
        555-318-4072
      </address>
      <address class="office">
        317 N Wexford Rd.<br>
        Suite 406<br>
        Mt. Verity, ST 00587<br>
        555-762-1938
      </address>
    </div>
  </section>
</main>
</body>
</html>
```